Great Opportunity !! Masters in Business Analytics College Course

the size is Full Page, with bleed*
8”x 10.75" plus 0.25" bleed.
please leave one inch for footer
the purpose is attract students to join this college program .
this is for students in USA .
college age of around 24 years old
I am looking for a flyer that is unique and shows creativity .
A flyer that people would want to look at it because it is unique.
you can choose either vector, text ,or picture.
if you do picture it should be a white USA citizen wearing a white solid shirt and not long hair

Target Market(s)

USA students about 23 in age to join this college program

Industry/Entity Type

education

Colors
0054AA
0677BA
7BADD7
CADEEF
E8F1F8
0094D4
00A9DD
6FCCEA
C7EBF8
E9F6FB

Requirements
Must have
• the text should not be crowded .. .. .. the ad should not be full of text
Should not have
• not have very large text .. it should not be a flyer that is full of text .. you have to figure out how to avoid looking at the ad and it is very busy with text

```html
<!DOCTYPE html>
<html lang="en">
<head>
<meta charset="utf-8">
<title>Master's in Business Analytics – Open House</title>
<link rel="stylesheet" href="https://fonts.googleapis.com/css2?family=Montserrat:wght@500;600;700&family=Oswald:wght@500;700&display=swap">
<style>
  :root {
    --paper: #ecebe8;
    --ink: #111111;
    --navy: #0054aa;
    --blue: #1a75bb;
    --cyan: #0094d4;
    --sky: #00a9dd;
    --light-sky: #6fccea;
    --pale: #c7ebf8;
    --teal-ink: #0b5e7e;
    --footer-bg: #232323;
    --footer-ink: #9a9a9a;
  }
  * { margin: 0; padding: 0; box-sizing: border-box; }
  html, body { width: 900px; height: 1200px; overflow: hidden; background: #ffffff; }
  .flyer {
    position: relative;
    width: 900px;
    height: 1200px;
    overflow: hidden;
    background: radial-gradient(ellipse at 50% 40%, #f4f3f1 0%, var(--paper) 70%, #e2e1de 100%);
    font-family: "Montserrat", Arial, sans-serif;
    color: var(--ink);
  }
  .headline {
    position: absolute;
    top: 28px; left: 0; width: 100%;
    text-align: center;
    font-size: 28px;
    font-weight: 500;
    line-height: 39px;
  }
  .headline-rule {
    position: absolute;
    top: 112px; left: 225px;
    width: 469px; height: 5px;
    background: var(--cyan);
  }
  .hero-art {
    position: absolute;
    top: 135px; left: 47px;
    width: 770px; height: 505px;
    border-radius: 46% 54% 40% 48% / 50% 42% 46% 50%;
    background:
      radial-gradient(ellipse at 78% 45%, var(--navy) 0%, var(--cyan) 32%, rgba(0,148,212,0) 60%),
      radial-gradient(ellipse at 30% 25%, #d8d8d8 0%, rgba(216,216,216,0) 40%),
      radial-gradient(ellipse at 50% 62%, #6c7d98 0%, #8fa3c0 22%, rgba(143,163,192,0) 45%),
      radial-gradient(ellipse at 25% 55%, var(--sky) 0%, var(--light-sky) 30%, rgba(111,204,234,0) 55%),
      radial-gradient(ellipse at 50% 50%, var(--pale) 0%, rgba(199,235,248,0) 75%);
  }
  .program-title {
    position: absolute;
    top: 655px; left: 0; width: 100%;
    text-align: center;
    font-size: 29px;
    font-weight: 600;
    line-height: 39px;
  }
  .program-title span { text-decoration: underline; text-underline-offset: 6px; text-decoration-thickness: 2px; }
  .program-title .mark { color: var(--sky); font-size: 22px; position: relative; top: -10px; line-height: 0; }
  .promise {
    position: absolute;
    top: 742px; left: 0; width: 100%;
    text-align: center;
    font-size: 28px;
    font-weight: 500;
    line-height: 41px;
    text-transform: uppercase;
  }
  .source {
    position: absolute;
    top: 826px; left: 0; width: 100%;
    text-align: center;
    font-size: 19px;
    font-weight: 500;
    color: var(--teal-ink);
  }
  .roles {
    position: absolute;
    top: 856px; left: 0; width: 100%;
    display: flex; justify-content: center; gap: 52px;
    font-size: 29px; font-weight: 500;
    color: var(--blue);
  }
  .hired-label {
    position: absolute;
    top: 907px; left: 0; width: 100%;
    text-align: center;
    font-size: 24px; font-weight: 600;
  }
  .employers {
    position: absolute;
    top: 937px; left: 0; width: 100%;
    display: flex; justify-content: center; gap: 26px;
    font-size: 29px; font-weight: 500;
    color: var(--blue);
  }
  .employers span { text-decoration: underline; text-underline-offset: 5px; text-decoration-thickness: 2px; }
  .pin-icon { position: absolute; top: 998px; left: 24px; width: 54px; height: 54px; }
  .open-house {
    position: absolute;
    top: 975px; left: 89px;
    font-family: "Oswald", Impact, sans-serif;
    font-weight: 700;
    font-size: 86px;
    line-height: 100px;
    white-space: nowrap;
    transform: scaleX(0.7);
    transform-origin: left center;
  }
  .event-box {
    position: absolute;
    top: 992px; left: 400px;
    width: 482px; height: 71px;
    border: 2px solid var(--ink);
    background: var(--paper);
  }
  .event-date {
    height: 34px;
    background: var(--ink);
    color: var(--light-sky);
    font-size: 26px; font-weight: 500;
    text-align: center;
    line-height: 34px;
  }
  .event-contact {
    text-align: center;
    font-size: 19px; font-weight: 500;
    line-height: 33px;
    white-space: nowrap;
  }
  .event-contact .email { color: var(--cyan); margin-left: 8px; letter-spacing: 0.5px; }
  .accreditation {
    position: absolute;
    top: 1066px; left: 17px;
    width: 866px; height: 27px;
    border-top: 2px solid var(--cyan);
    border-bottom: 2px solid var(--cyan);
    text-align: center;
    font-size: 17px; font-weight: 500;
    line-height: 23px;
    white-space: nowrap;
  }
  .accreditation .mark { color: var(--sky); margin-right: 6px; }
  .format-tag {
    position: absolute;
    top: 1093px; left: 262px;
    width: 378px; height: 26px;
    background: var(--sky);
    color: #ffffff;
    font-size: 17px; font-weight: 700;
    text-align: center;
    line-height: 26px;
    letter-spacing: 0.5px;
  }
  .footer {
    position: absolute;
    bottom: 0; left: 0;
    width: 100%; height: 71px;
    background: var(--footer-bg);
    color: var(--footer-ink);
    font-family: "Oswald", Impact, sans-serif;
    font-weight: 500;
    font-size: 25px;
    letter-spacing: 15px;
    text-align: center;
    line-height: 71px;
    padding-left: 15px;
  }
</style>
</head>
<body>
  <main class="flyer">
    <h1 class="headline">Do you have an ANALYTICAL MIND?<br>Are you seeking a PROFITABLE CAREER?</h1>
    <div class="headline-rule"></div>

    <div class="hero-art" role="img" aria-label="Illustration: blue profile silhouette of a head containing a map and city skyline with circuit lines, a stack of books, clouds, a laptop, a bar chart, a globe and silhouettes of students"></div>

    <h2 class="program-title">
      <span>A Master's in Business Analytics-</span><br>
      <span>Ridgewater State University</span> <b class="mark">**</b>
    </h2>

    <p class="promise">Can prepare you for in-demand jobs with a<br>median salary of $100K+</p>
    <p class="source">(the National Labor Data Office 2023)</p>

    <div class="roles">
      <span>BI Developer</span>
      <span>Data Analyst</span>
      <span>Data Scientist</span>
    </div>

    <p class="hired-label">GRADUATES WERE HIRED AT:</p>
    <div class="employers">
      <span>Veltrix</span>
      <span>Harlow</span>
      <span>Quorra</span>
      <span>Voltane</span>
    </div>

    <svg class="pin-icon" viewBox="0 0 54 54" aria-hidden="true">
      <circle cx="27" cy="27" r="27" fill="#0094d4"/>
      <path d="M27 12c-6 0-10.5 4.5-10.5 10.3 0 7.5 10.5 19 10.5 19s10.5-11.5 10.5-19C37.5 16.5 33 12 27 12z" fill="#ffffff"/>
      <circle cx="27" cy="22.5" r="4.2" fill="#0094d4"/>
    </svg>
    <div class="open-house">OPEN HOUSE</div>

    <div class="event-box">
      <div class="event-date">Wednesday, April 20, 7:30 pm.</div>
      <div class="event-contact">Email for link<span class="email">msba.info@ridgewater.edu</span></div>
    </div>

    <p class="accreditation"><span class="mark">**</span>GBSA Accreditation. This distinction is held by only 5% of business schools globally.</p>
    <div class="format-tag">HYBRID / ONE WEEKLY SESSION</div>

    <footer class="footer">ONE INCH FOR THE FOOTER</footer>
  </main>
</body>
</html>
```